Corporate Branded Documents - IT Provider - On-going work

Hi, I'm Tom a Director of Harbourline IT Care a UK Based IT & Telecoms support firm. We've been trading for 12 years now and feel its time for a lick of paint. We have a logo, website etc but would like someone to create some standard documents for us.

- A PDF Proposal Template - We currently don't send our customers proposals as we have nothing that looks good.
- A Quote Template PDF - Example Attached
- A Order Template PDF - Example Attached
- A Invoice Template PDF - Example Attached
- A Generic Document PDF - Something we can use for customer application forms, NDA Agreements, Terms & Conditions etc

Our website can be found at www.harbourlineitcare.co.uk - here you'll get a feel for our branding. I've also attached 2 example documents - as well as our currently used documents. Hopefully you guys can see why it needs improving.

We'd also like to work with someone long term, these documents are a start but we'd like to make sure all the work we do looks and feels as smart as possible, so there is plenty of additional work available.

None of these templates need to be Print ready, 99% of the time it will be viewed digitally, so high resolution designs are best

Thanks,

Tom

Target Market(s)

Corporate & Educational Customers

Industry/Entity Type

It Support

Font styles to use
Sans Serif

Colors
ec1f27
0692cd
ffffff

```html
<!DOCTYPE html>
<html lang="en">
<head>
<meta charset="utf-8">
<title>Harbourline IT Care – Generic Document</title>
<link href="https://fonts.googleapis.com/css2?family=Carlito:ital,wght@0,400;0,700;1,400&display=swap" rel="stylesheet">
<style>
  :root {
    --brand-blue: #0692cd;
    --heading-teal: #1a7896;
    --body-text: #555555;
    --panel-grey: #e8e8e8;
    --page-white: #ffffff;
    --rule-grey: #9a9a9a;
    --number-dark: #333333;
  }
  * { margin: 0; padding: 0; box-sizing: border-box; }
  html, body {
    width: 851px;
    height: 1200px;
    overflow: hidden;
    background: var(--page-white);
  }
  .page {
    position: relative;
    width: 851px;
    height: 1200px;
    font-family: "Carlito", "Calibri", sans-serif;
    color: var(--body-text);
    font-size: 19px;
    line-height: 31.5px;
  }
  .brand {
    position: absolute;
    top: 22px;
    right: 26px;
  }
  .brand-name {
    font-weight: 700;
    font-size: 26px;
    line-height: 1;
    color: var(--brand-blue);
  }
  .column {
    position: absolute;
    top: 124px;
    width: 346px;
  }
  .column-left { left: 48px; }
  .column-right { left: 463px; }
  .subtitle {
    font-weight: 700;
    font-size: 22px;
    line-height: 31.5px;
    color: var(--heading-teal);
  }
  .body-copy {
    text-align: justify;
    hyphens: none;
  }
  .body-copy + .body-copy { margin-top: 31.5px; }
  .callout {
    margin: 29px -6px 28px -1px;
    background: var(--panel-grey);
    padding: 19px 26px 19px 22px;
    font-style: italic;
    text-align: justify;
  }
  .footer {
    position: absolute;
    right: 26px;
    top: 1155px;
    display: flex;
    align-items: center;
    font-size: 19px;
    line-height: 1;
  }
  .footer-label { padding-right: 10px; }
  .footer-divider {
    width: 1px;
    height: 34px;
    background: var(--rule-grey);
  }
  .page-number {
    padding-left: 10px;
    font-size: 22px;
    color: var(--number-dark);
  }
</style>
</head>
<body>
<div class="page">
  <header class="brand">
    <span class="brand-name">Harbourline IT Care</span>
  </header>

  <section class="column column-left">
    <h2 class="subtitle">Subtitle Here</h2>
    <p class="body-copy">Lorem Ipsum is simply dummy text of the printing and typesetting industry. Lorem Ipsum has been the industry's industry. Lorem Ipsum has been the finishLorem Ipsum is simply dummy text of the printing and typesetting industry. Lorem Ipsum has been the industry's industry. Lorem Ipsum has been the finishLorem Ipsum is simply dummy text of the printing and typesetting industry. Lorem Ipsum has been the industry's industry. Lorem Ipsum has been the finishLorem Ipsum is simply dummy text of the printing and typesetting industry. Lorem Ipsum has been the industry's industry. Lorem Ipsum has been the finish.</p>
    <p class="body-copy">Lorem Ipsum is simply dummy text of the printing and typesetting industry. Lorem Ipsum has been the industry's industry. Lorem Ipsum has been the finishLorem Ipsum is simply dummy text of the printing and typesetting industry. Lorem Ipsum has been the industry's industry. Lorem Ipsum has been the finishLorem Ipsum is simply dummy text of the printing and typesetting industry. Lorem Ipsum has been the industry's industry.</p>
  </section>

  <section class="column column-right">
    <p class="body-copy">Lorem Ipsum is simply dummy text of the printing and typesetting industry. Lorem Ipsum has been the industry's industry.</p>
    <aside class="callout">Lorem Ipsum is simply dummy text of the printing and typesetting industry. Lorem Ipsum has been the industry's industry. Lorem Ipsum has been the finishLorem Ipsum is simply dummy text of the printing and typesetting industry. Lorem Ipsum has been the industry's industry. Lorem Ipsum is simply dummy text of the printing and typesetting industry. Lorem Ipsum has been the industry's industry.</aside>
    <p class="body-copy">Lorem Ipsum has been the finishLorem Ipsum is simply dummy text of the printing and typesetting industry. Lorem Ipsum has been the industry's industry. Lorem Ipsum has been the finishLorem Ipsum is simply dummy text of the printing and typesetting industry. Lorem Ipsum has been the industry's industry. Lorem Ipsum has been the finishLorem Ipsum.</p>
  </section>

  <footer class="footer">
    <span class="footer-label">Confendtial</span>
    <span class="footer-divider"></span>
    <span class="page-number">1</span>
  </footer>
</div>
</body>
</html>
```